Pop-up Banner

Would like a design for a pop-up 85 x 206cm banner for a trade show. (from norla press)
We would like "our logo" (brightwave holdings) - then the tagline - "Your Trusted Partner in Data-Driven Decisions"
*Supporting Bullets*
Unified data, analytics & AI
Trusted insights, faster outcomes
Real-time intelligence at scale
Enterprise-ready, secure solutions
Clarity from data complexity
trusted by...some company logos
Partners with : partner logo
Our Colours: #FFA300, #3D4176, #FDD16E, #F87C57, #A68118, #1C2F36

```html
<!DOCTYPE html>
<html lang="en">
<head>
<meta charset="utf-8">
<title>Brightwave Holdings – Pop-up Banner</title>
<link rel="stylesheet" href="https://fonts.googleapis.com/css2?family=Exo+2:ital,wght@0,700;1,700;1,800&family=Open+Sans:wght@400;600&display=swap">
<style>
  :root {
    --orange: #FFA300;
    --amber: #FDB52A;
    --navy: #3D4176;
    --sand: #FDD16E;
    --coral: #F87C57;
    --ochre: #A68118;
    --ink: #1C2F36;
    --slate: #27353C;
    --backdrop: #E2970F;
    --steel: #C9CCCF;
    --white: #FFFFFF;
  }
  * { box-sizing: border-box; margin: 0; padding: 0; }
  html, body { width: 1200px; height: 800px; overflow: hidden; }
  body { background: var(--backdrop); position: relative; font-family: "Open Sans", sans-serif; }

  .banner { position: absolute; left: 445px; top: 20px; width: 310px; height: 760px; }
  .banner__rail { position: absolute; left: 0; top: 0; width: 100%; height: 6px; background: var(--steel); }

  .banner__photo {
    position: absolute; left: 0; top: 150px; width: 100%; height: 320px;
    background: radial-gradient(ellipse at 55% 45%, #6d5a52 0%, #3a4a52 40%, #1e3a44 75%, #1a2b33 100%);
  }

  .banner__header {
    position: absolute; left: 0; top: 6px; width: 100%; height: 192px;
    background: var(--slate); border-bottom-right-radius: 44px;
    padding: 30px 18px 0 24px;
  }
  .brand { display: flex; align-items: center; gap: 12px; }
  .brand__dot { width: 50px; height: 50px; border-radius: 50%; border: 8px solid var(--orange); flex: none; }
  .brand__name {
    font-family: "Exo 2", sans-serif; font-weight: 700; color: var(--orange);
    font-size: 21px; line-height: 23px; letter-spacing: 1px; text-transform: uppercase;
  }
  .tagline {
    margin-top: 18px; font-family: "Exo 2", sans-serif; font-style: italic; font-weight: 700;
    color: var(--white); font-size: 22px; line-height: 27px;
  }

  .banner__benefits {
    position: absolute; left: 0; top: 438px; width: 100%; height: 170px;
    background: var(--amber); border-radius: 30px 30px 0 0;
    padding: 22px 18px 0 26px;
  }
  .benefits { list-style: none; }
  .benefits li {
    display: flex; align-items: center; gap: 10px; height: 24px;
    font-family: "Exo 2", sans-serif; font-style: italic; font-weight: 800;
    font-size: 12.5px; color: var(--ink);
  }
  .benefits svg { flex: none; }

  .banner__footer {
    position: absolute; left: 0; top: 590px; width: 100%; height: 136px;
    background: var(--slate); border-radius: 26px 26px 0 0;
    text-align: center; padding-top: 10px; color: var(--white);
  }
  .footer__label { font-weight: 600; font-size: 11px; }
  .logo-grid { display: grid; grid-template-columns: repeat(3, 1fr); row-gap: 6px; margin: 8px 20px 10px; }
  .logo-name { font-family: "Open Sans", sans-serif; font-weight: 600; font-size: 12px; display: flex; align-items: center; justify-content: center; gap: 4px; }
  .logo-name .mark { width: 8px; height: 8px; display: inline-block; }
  .partner-row { display: flex; justify-content: space-around; margin: 8px 14px 0; }
  .c-teal { color: #2BB3A8; } .c-teal .mark { background: #2BB3A8; border-radius: 50%; }
  .c-grey { color: #AAB3B8; } .c-grey .mark { background: #AAB3B8; }
  .c-blue { color: #2A9AD8; } .c-blue .mark { background: #2A9AD8; border-radius: 50%; }
  .c-pink { color: #D84A72; } .c-pink .mark { background: #D84A72; }
  .c-purple { color: #7A3FA0; }
  .c-red { color: #D9452B; }
  .c-green { color: #3DB54A; } .c-green .mark { background: #3DB54A; border-radius: 50%; }

  .banner__stand {
    position: absolute; left: -4px; top: 726px; width: 318px; height: 26px;
    background: linear-gradient(#e4e6e8, #b8bcbf 60%, #9fa3a6);
    border-radius: 2px;
  }
  .banner__foot { position: absolute; top: 750px; width: 28px; height: 8px; background: #b0b4b7; border-radius: 0 0 4px 4px; }
  .banner__foot--left { left: 40px; }
  .banner__foot--right { right: 40px; }
</style>
</head>
<body>
  <div class="banner">
    <div class="banner__rail"></div>
    <div class="banner__photo" role="img" aria-label="Photo of a thoughtful analyst in glasses in front of glowing data screens"></div>

    <header class="banner__header">
      <div class="brand">
        <span class="brand__dot"></span>
        <span class="brand__name">Brightwave<br>Holdings</span>
      </div>
      <p class="tagline">Your Trusted Partner in<br>Data-Driven Decisions</p>
    </header>

    <section class="banner__benefits">
      <ul class="benefits">
        <li><svg width="13" height="13" viewBox="0 0 13 13"><rect x="1" y="2" width="10" height="10" fill="none" stroke="#1C2F36" stroke-width="1.6"/><path d="M3.5 6.5l2.5 2.5 6-7" fill="none" stroke="#1C2F36" stroke-width="1.8"/></svg>Unified data, analytics &amp; AI</li>
        <li><svg width="13" height="13" viewBox="0 0 13 13"><rect x="1" y="2" width="10" height="10" fill="none" stroke="#1C2F36" stroke-width="1.6"/><path d="M3.5 6.5l2.5 2.5 6-7" fill="none" stroke="#1C2F36" stroke-width="1.8"/></svg>Trusted insights, faster outcomes</li>
        <li><svg width="13" height="13" viewBox="0 0 13 13"><rect x="1" y="2" width="10" height="10" fill="none" stroke="#1C2F36" stroke-width="1.6"/><path d="M3.5 6.5l2.5 2.5 6-7" fill="none" stroke="#1C2F36" stroke-width="1.8"/></svg>Real-time intelligence at scale</li>
        <li><svg width="13" height="13" viewBox="0 0 13 13"><rect x="1" y="2" width="10" height="10" fill="none" stroke="#1C2F36" stroke-width="1.6"/><path d="M3.5 6.5l2.5 2.5 6-7" fill="none" stroke="#1C2F36" stroke-width="1.8"/></svg>Enterprise-ready, secure solutions</li>
        <li><svg width="13" height="13" viewBox="0 0 13 13"><rect x="1" y="2" width="10" height="10" fill="none" stroke="#1C2F36" stroke-width="1.6"/><path d="M3.5 6.5l2.5 2.5 6-7" fill="none" stroke="#1C2F36" stroke-width="1.8"/></svg>Clarity from data complexity</li>
      </ul>
    </section>

    <footer class="banner__footer">
      <p class="footer__label">Trusted By:</p>
      <div class="logo-grid">
        <span class="logo-name c-teal"><span class="mark"></span>Corvane</span>
        <span class="logo-name c-grey"><span class="mark"></span>Pemblo</span>
        <span class="logo-name c-blue"><span class="mark"></span>Tarrow</span>
        <span class="logo-name c-grey">Quillon</span>
        <span class="logo-name c-pink"><span class="mark"></span>Dunmere</span>
        <span class="logo-name c-purple">Velmora</span>
      </div>
      <p class="footer__label">Partners with:</p>
      <div class="partner-row">
        <span class="logo-name c-red">Ostrana</span>
        <span class="logo-name c-green"><span class="mark"></span>clearpath labs</span>
        <span class="logo-name c-grey"><span class="mark"></span>Northgrid</span>
      </div>
    </footer>

    <div class="banner__stand"></div>
    <div class="banner__foot banner__foot--left"></div>
    <div class="banner__foot banner__foot--right"></div>
  </div>
</body>
</html>
```